I need a book cover design for my book "Roaming Quartets." It is a non-fiction book focused on answering the question of whether American evangelicals look more like the Quartets than Jesus.

The subtitle is "The Curious Habits of Norway's Traveling Fiddlers and Their Seaside Rivals." The author name is Dorian Whitlock.

I will be publishing this as an ebook and paperback.

I am open to all ideas, but will share the only thought I had as a possible design. In the title, the third letter in both words is "A." I thought about the idea of having the "A" in "Roaming" have a halo and the "A" in "Quartets" somehow seem to be a shadow of that first "A" but have devil horns instead of a halo. Again, I'm not sold on that, but am sharing it as one design possibility.

I am not interested in the book cover design having a cheesy religious look to it (as many do). I am more interested in it looking like a professional non-fiction cover.

```html
<!DOCTYPE html>
<html lang="en">
<head>
<meta charset="utf-8">
<title>Roaming Quartets — Cover Spread</title>
<link href="https://fonts.googleapis.com/css2?family=Allura&family=Josefin+Sans:wght@600;700&display=swap" rel="stylesheet">
<style>
  :root {
    --cover-red: #be1e2d;
    --paper-white: #ffffff;
    --blush: #f6e4e6;
  }
  html, body {
    margin: 0;
    padding: 0;
    overflow: hidden;
    background: var(--paper-white);
  }
  .spread {
    position: relative;
    width: 1200px;
    height: 910px;
    overflow: hidden;
    background: var(--paper-white);
  }
  .back-cover,
  .front-cover {
    position: absolute;
    top: 17px;
    width: 468px;
    height: 883px;
    background: var(--cover-red);
  }
  .back-cover { left: 120px; }
  .front-cover { left: 607px; }

  .emblem-area {
    position: absolute;
    left: 87px;
    top: 269px;
    width: 305px;
    height: 326px;
    border-radius: 40px;
    background: linear-gradient(160deg, var(--paper-white), var(--blush));
  }

  .title {
    position: absolute;
    left: 0;
    width: 468px;
    top: 128px;
    margin: 0;
    text-align: center;
    font-family: "Allura", cursive;
    font-weight: 400;
    font-size: 74px;
    line-height: 1;
    color: var(--paper-white);
    white-space: nowrap;
    text-shadow: 0 0 1px var(--paper-white);
  }
  .subtitle {
    position: absolute;
    left: 0;
    width: 468px;
    top: 248px;
    margin: 0;
    text-align: center;
    font-family: "Josefin Sans", sans-serif;
    font-weight: 700;
    font-size: 19px;
    line-height: 22.5px;
    color: var(--paper-white);
    text-transform: uppercase;
  }
  .cross-upright {
    position: absolute;
    left: 202px;
    top: 360px;
    width: 63px;
    height: 523px;
    background: var(--paper-white);
  }
  .cross-beam {
    position: absolute;
    left: 0;
    top: 535px;
    width: 468px;
    height: 64px;
    background: var(--paper-white);
  }
  .author {
    position: absolute;
    left: 0;
    top: 535px;
    width: 468px;
    height: 64px;
    margin: 0;
    display: flex;
    align-items: center;
    justify-content: center;
    padding-top: 5px;
    box-sizing: border-box;
    font-family: "Josefin Sans", sans-serif;
    font-weight: 600;
    font-size: 31px;
    color: var(--cover-red);
    text-transform: uppercase;
    white-space: nowrap;
  }
</style>
</head>
<body>
<div class="spread">
  <section class="back-cover">
    <div class="emblem-area" role="img" aria-label="White rounded hexagon emblem with a red cross"></div>
  </section>

  <section class="front-cover">
    <h1 class="title">Roaming Quartets</h1>
    <p class="subtitle">The Curious Habits of Norway's<br>Traveling Fiddlers and<br>Their Seaside Rivals</p>
    <div class="cross-upright"></div>
    <div class="cross-beam"></div>
    <p class="author">Dorian Whitlock</p>
  </section>
</div>
</body>
</html>
```